Composite decking sales poster

Poster advertising our brand of decking and our industry-best warranty.
Poster dimensions 1200mm wide x 400mm high.
50 Year Stain and Fade Warranty.
Ultra-Low Maintenance.
Environmentally Friendly Made from Recycled Materials.
Website: https://velmorboards.com.au
Phone: 1300 482 937
*** Uploaded pictures are optional to use ***
Must list website, phone number and logos.

```html
<!DOCTYPE html>
<html lang="en">
<head>
<meta charset="utf-8">
<title>Velmor Boards – Lasting Satisfaction</title>
<link href="https://fonts.googleapis.com/css2?family=Montserrat:wght@400;500;700&display=swap" rel="stylesheet">
<style>
  :root {
    --backdrop: #4a4a4a;
    --paper: #ffffff;
    --navy: #4b6194;
    --ink: #3b3b3b;
    --badge: #5a5753;
    --deck-warm-1: #6b3f22;
    --deck-warm-2: #a8744c;
    --deck-grey-1: #8d8d8d;
    --pool-blue: #3f7fb4;
    --boards-dark: #4a3d36;
  }
  * { box-sizing: border-box; margin: 0; padding: 0; }
  html, body {
    width: 1200px; height: 515px; overflow: hidden;
    background: var(--backdrop);
    font-family: "Montserrat", sans-serif;
  }
  .poster {
    position: absolute; left: 0; top: 57px;
    width: 1200px; height: 400px;
    background: var(--paper); overflow: hidden;
  }
  .poster-shapes { position: absolute; inset: 0; }
  .brand {
    position: absolute; left: 30px; top: 40px;
    display: flex; align-items: center; gap: 10px;
    color: var(--navy); font-weight: 700; font-size: 27px; letter-spacing: 0.5px;
  }
  .brand-mark { width: 22px; height: 22px; background: var(--navy); }
  .headline {
    position: absolute; left: 208px; top: 116px;
    font-size: 27px; font-weight: 400; color: var(--ink); letter-spacing: 0.3px;
    white-space: nowrap;
  }
  .headline strong { font-weight: 700; color: var(--navy); }
  .intro {
    position: absolute; left: 332px; top: 166px; width: 260px;
    font-size: 11.5px; line-height: 21px; color: var(--ink);
  }
  .features {
    position: absolute; left: 332px; top: 240px; list-style: none;
    font-size: 11.5px; line-height: 21px; color: var(--ink);
  }
  .features li { position: relative; padding-left: 24px; }
  .features .tick { position: absolute; left: 0; top: 4px; width: 13px; height: 13px; }
  .contact {
    position: absolute; left: 591px; top: 356px;
    display: flex; align-items: center; gap: 6px; white-space: nowrap;
  }
  .contact-icon { width: 16px; height: 16px; }
  .contact-web { font-size: 19px; color: var(--ink); margin-right: 14px; }
  .contact-phone { font-size: 19px; font-weight: 700; color: var(--navy); }
  .badges { position: absolute; left: 1031px; top: 312px; display: flex; gap: 13px; }
  .badge {
    width: 63px; height: 62px; border: 2px solid var(--badge); border-radius: 4px;
    padding: 3px; background: var(--paper);
  }
  .badge-face { width: 100%; height: 100%; background: var(--badge); border-radius: 2px; }
</style>
</head>
<body>
<main class="poster">
  <svg class="poster-shapes" width="1200" height="400" viewBox="0 0 1200 400">
    <defs>
      <linearGradient id="terraceTones" x1="0" y1="0" x2="1" y2="1">
        <stop offset="0" stop-color="var(--deck-warm-1)"/>
        <stop offset="0.6" stop-color="#7a6a55"/>
        <stop offset="1" stop-color="var(--deck-warm-2)"/>
      </linearGradient>
      <linearGradient id="poolTones" x1="0" y1="0" x2="1" y2="0">
        <stop offset="0" stop-color="var(--deck-grey-1)"/>
        <stop offset="0.55" stop-color="#b9b9b9"/>
        <stop offset="0.7" stop-color="var(--pool-blue)"/>
        <stop offset="1" stop-color="#5b9bcc"/>
      </linearGradient>
      <radialGradient id="boardTones">
        <stop offset="0" stop-color="#5e4f46"/>
        <stop offset="1" stop-color="var(--boards-dark)"/>
      </radialGradient>
    </defs>
    <path role="img" aria-label="Covered timber terrace with outdoor sofa, barbecue, dining table and garden view"
          d="M470,0 C560,8 600,90 660,165 C720,235 760,278 840,278 L1200,278 L1200,0 Z"
          fill="url(#terraceTones)"/>
    <path role="img" aria-label="Grey composite pool deck seen from above with a towel, laptop and coffee cup"
          d="M0,191 L95,191 C150,191 195,228 240,290 C290,360 350,396 460,400 L0,400 Z"
          fill="url(#poolTones)"/>
    <circle role="img" aria-label="Close-up of dark herringbone composite decking boards"
            cx="686" cy="241" r="96" fill="url(#boardTones)" stroke="#ffffff" stroke-width="3"/>
    <line x1="214" y1="151" x2="648" y2="151" stroke="var(--navy)" stroke-width="1.2"/>
    <circle cx="214" cy="151" r="2.8" fill="var(--navy)"/>
    <line x1="591" y1="349" x2="1019" y2="349" stroke="var(--navy)" stroke-width="1.2"/>
    <circle cx="591" cy="349" r="2.8" fill="var(--navy)"/>
  </svg>

  <div class="brand"><span class="brand-mark"></span>VELMOR BOARDS</div>

  <h1 class="headline">LASTING <strong>SATISFACTION.</strong></h1>

  <p class="intro">The industry’s first 50-Year Stain and Fade Warranty and Lifetime Performance Warranty.</p>

  <ul class="features">
    <li><svg class="tick" viewBox="0 0 13 13"><rect x="0.7" y="0.7" width="11.6" height="11.6" fill="none" stroke="var(--navy)" stroke-width="1.4"/><path d="M3,6.5 L5.6,9 L11.5,2" fill="none" stroke="var(--navy)" stroke-width="1.8"/></svg>50 Year Stain and Fade Warranty.</li>
    <li><svg class="tick" viewBox="0 0 13 13"><rect x="0.7" y="0.7" width="11.6" height="11.6" fill="none" stroke="var(--navy)" stroke-width="1.4"/><path d="M3,6.5 L5.6,9 L11.5,2" fill="none" stroke="var(--navy)" stroke-width="1.8"/></svg>Ultra-Low Maintenance.</li>
    <li><svg class="tick" viewBox="0 0 13 13"><rect x="0.7" y="0.7" width="11.6" height="11.6" fill="none" stroke="var(--navy)" stroke-width="1.4"/><path d="M3,6.5 L5.6,9 L11.5,2" fill="none" stroke="var(--navy)" stroke-width="1.8"/></svg>Environmentally Friendly Made<br>from Recycled Materials.</li>
  </ul>

  <div class="contact">
    <svg class="contact-icon" viewBox="0 0 16 16"><circle cx="8" cy="8" r="8" fill="var(--navy)"/><path d="M5.5,4 L5.5,12 L7.6,10 L9.2,13 L10.4,12.4 L8.9,9.5 L11.5,9.3 Z" fill="#fff"/></svg>
    <span class="contact-web">velmorboards.com.au</span>
    <svg class="contact-icon" viewBox="0 0 16 16"><circle cx="8" cy="8" r="8" fill="var(--navy)"/><path d="M5.2,4 C4.4,4.6 4.2,5.6 4.8,7 C5.6,9 7.2,10.8 9,11.5 C10.3,12 11.3,11.7 11.9,11 L10.4,9.5 L9.3,10.1 C8.2,9.5 7,8.3 6.4,7.1 L7,6 Z" fill="#fff"/></svg>
    <span class="contact-phone">1300 482 937</span>
  </div>

  <div class="badges">
    <div class="badge"><div class="badge-face"></div></div>
    <div class="badge"><div class="badge-face"></div></div>
  </div>
</main>
</body>
</html>
```